OKU professional cleaner

this professional multi-surface cleaner is intended for professionals.
Powerful degreaser. We would like to focus on the professional side.
We already have a range of disinfectants, and we would like a design close to this range but still distinct. The name is OKU and yhe logo is NUVAShine.the visible part of the label is 55mm and will be affixed to a round bottle with trigger .

Target Market(s)

professional

```html
<!DOCTYPE html>
<html lang="en">
<head>
<meta charset="utf-8">
<title>OKU Professional Multi-surface Cleaner – Label</title>
<link rel="stylesheet" href="https://fonts.googleapis.com/css2?family=Fira+Sans+Condensed:wght@300;400;600;700&display=swap">
<style>
  :root {
    --canvas-bg: #f5f5f5;
    --brand-red: #da1c25;
    --sky-blue: #74c3e8;
    --pale-blue: #d7ecf8;
    --white: #ffffff;
    --ink: #2b2b2b;
  }
  * { margin: 0; padding: 0; box-sizing: border-box; }
  html, body {
    width: 900px;
    height: 1200px;
    overflow: hidden;
    background: var(--canvas-bg);
  }
  .canvas {
    position: relative;
    width: 900px;
    height: 1200px;
    background: var(--canvas-bg);
  }
  .label {
    position: absolute;
    left: 200px;
    top: 30px;
    width: 500px;
    height: 1140px;
    overflow: hidden;
    font-family: "Fira Sans Condensed", sans-serif;
  }
  .label-ground {
    position: absolute;
    inset: 0;
    width: 500px;
    height: 1140px;
  }
  .range-band {
    position: absolute;
    top: 0;
    left: 0;
    width: 500px;
    height: 104px;
    display: flex;
    align-items: center;
    justify-content: center;
    color: var(--white);
    font-weight: 700;
    font-size: 64px;
    letter-spacing: 0.5px;
  }
  .product-name {
    position: absolute;
    left: 48px;
    top: 250px;
    width: 310px;
    height: 200px;
    overflow: visible;
  }
  .product-name text {
    font-family: "Fira Sans Condensed", sans-serif;
    font-weight: 600;
    font-size: 204px;
    fill: var(--brand-red);
    stroke: var(--white);
    stroke-width: 5px;
    paint-order: stroke;
  }
  .usage-icon {
    position: absolute;
    left: 364px;
    top: 148px;
    width: 112px;
    height: 140px;
  }
  .descriptions {
    position: absolute;
    left: 57px;
    top: 452px;
    color: var(--ink);
    font-weight: 400;
    font-size: 41px;
    line-height: 57.5px;
  }
  .descriptions .lang {
    font-size: 33px;
  }
  .brand-name {
    position: absolute;
    left: 0;
    top: 990px;
    width: 500px;
    text-align: center;
    color: var(--white);
    font-weight: 400;
    font-size: 60px;
    line-height: 1;
  }
</style>
</head>
<body>
  <main class="canvas">
    <section class="label" aria-label="OKU professional multi-surface cleaner label">
      <svg class="label-ground" viewBox="0 0 500 1140" aria-hidden="true">
        <defs>
          <linearGradient id="body-fade" x1="0" y1="0" x2="0" y2="1">
            <stop offset="0" stop-color="var(--sky-blue)"/>
            <stop offset="0.45" stop-color="var(--pale-blue)"/>
            <stop offset="0.8" stop-color="var(--white)"/>
            <stop offset="1" stop-color="var(--white)"/>
          </linearGradient>
        </defs>
        <rect x="0" y="100" width="500" height="840" fill="url(#body-fade)"/>
        <rect x="0" y="0" width="500" height="104" fill="var(--brand-red)"/>
        <path d="M0 945 C40 900 80 878 120 880 C170 882 200 935 250 935 C300 935 340 878 395 878 C440 878 480 910 500 935 V1140 H0 Z" fill="var(--brand-red)"/>
      </svg>

      <div class="range-band">PROFESSIONAL</div>

      <svg class="product-name" viewBox="0 0 310 200" aria-label="OKU">
        <text x="4" y="182" textLength="300" lengthAdjust="spacingAndGlyphs">OKU</text>
      </svg>

      <svg class="usage-icon" viewBox="0 0 112 140" role="img" aria-label="Illustration of a hand wiping with a cloth and a sparkle">
        <rect x="4" y="20" width="104" height="112" rx="20" fill="var(--brand-red)"/>
      </svg>

      <p class="descriptions">
        Multi-surface<br>cleaner <span class="lang">FR</span><br>
        Multi-surface<br>cleaner<br>
        Multi-surface<br>cleaner <span class="lang">DE</span>
      </p>

      <p class="brand-name">NUVAShine</p>
    </section>
  </main>
</body>
</html>
```